RKW Automotive needs a catchy banner design

We need a design for a banner to be displayed on the fence in the outfield of a baseball stadium to show off our company and have people interested in what we do. We need something catchy that's going to attract people to look over at our banner.
We are a
Complete Automotive Service Company
Tires - Service - Repair - Diesel
We are in a Town called Briar-Hollow
(555)314-2096 we would like the phone number to be a descent size so when you are in the stands you can read it.
I have attached what we came up with but like I said we need it to pop more and make the viewer that's looking at it want to look us up.
The Banner size is 24ft long and 10ft tall

```html
<!DOCTYPE html>
<html lang="en">
<head>
<meta charset="utf-8">
<title>RKW Automotive – Outfield Banner</title>
<link rel="stylesheet" href="https://fonts.googleapis.com/css2?family=Anton&family=Exo+2:wght@700&family=Montserrat:wght@700&family=Oswald:wght@500;700&display=swap">
<style>
  :root {
    --page: #ffffff;
    --banner-yellow: #fcf891;
    --band-white: #ffffff;
    --band-shadow: #d9d48a;
    --accent-orange: #e2700f;
    --box-orange: #de5a1e;
    --ink: #141414;
    --brand-blue: #1a6fe0;
    --sky-blue: #0b8ad6;
    --phone-top: #0a7fd8;
    --phone-bottom: #1b3a8c;
    --photo-light: #9a9a96;
    --photo-dark: #3c3d3f;
  }
  html, body {
    margin: 0;
    padding: 0;
    width: 1200px;
    height: 1200px;
    overflow: hidden;
    background: var(--page);
  }
  .canvas {
    position: relative;
    width: 1200px;
    height: 1200px;
  }
  .banner {
    position: absolute;
    left: 80px;
    top: 382px;
    width: 1040px;
    height: 434px;
    outline: 1px solid #d6d6c8;
  }
  .banner svg { display: block; width: 100%; height: 100%; }
  .brand-name { font-family: "Oswald", sans-serif; font-weight: 700; fill: var(--brand-blue); }
  .tagline-small { font-family: "Oswald", sans-serif; font-weight: 500; }
  .tagline-big { font-family: "Oswald", sans-serif; font-weight: 700; }
  .ink { fill: var(--ink); }
  .sky { fill: var(--sky-blue); }
  .service-label { font-family: "Exo 2", sans-serif; font-weight: 700; fill: var(--ink); }
  .service-box { fill: none; stroke: var(--box-orange); stroke-width: 3; }
  .phone-number { font-family: "Anton", sans-serif; fill: #ffffff; }
  .town { font-family: "Montserrat", sans-serif; font-weight: 700; fill: var(--ink); letter-spacing: 4px; }
</style>
</head>
<body>
<div class="canvas">
  <div class="banner">
    <svg viewBox="0 0 1674 698" xmlns="http://www.w3.org/2000/svg">
      <defs>
        <linearGradient id="phoneFill" x1="0" y1="0" x2="0" y2="1">
          <stop offset="0" stop-color="var(--phone-top)"/>
          <stop offset="1" stop-color="var(--phone-bottom)"/>
        </linearGradient>
        <linearGradient id="photoFill" x1="0" y1="0" x2="0" y2="1">
          <stop offset="0" stop-color="var(--photo-light)"/>
          <stop offset="1" stop-color="var(--photo-dark)"/>
        </linearGradient>
      </defs>

      <rect class="banner-bg" x="0" y="0" width="1674" height="698" fill="var(--banner-yellow)"/>

      <polygon class="accent-slash" points="1036,0 1136,0 1086,185 1020,185" fill="var(--accent-orange)"/>

      <rect class="band-shadow" x="0" y="45" width="1060" height="17" fill="var(--band-shadow)" opacity="0.6"/>
      <polygon class="headline-band" points="0,62 1091,62 1031,269 0,269" fill="var(--band-white)"/>

      <text class="brand-name" x="226" y="178" font-size="112" text-anchor="middle" textLength="270" lengthAdjust="spacingAndGlyphs">RKW</text>
      <text class="brand-name" x="226" y="236" font-size="42" text-anchor="middle" textLength="270" lengthAdjust="spacingAndGlyphs">AUTOMOTIVE</text>

      <text class="tagline-small ink" x="496" y="150" font-size="40">From</text>
      <text class="tagline-big ink" x="589" y="150" font-size="82" textLength="447" lengthAdjust="spacingAndGlyphs">OIL CHANGES</text>
      <text class="tagline-small sky" x="433" y="245" font-size="40">To</text>
      <text class="tagline-big sky" x="488" y="245" font-size="82" textLength="538" lengthAdjust="spacingAndGlyphs">CUSTOM BUILDS</text>

      <g class="services">
        <rect class="service-box" x="52" y="325" width="217" height="73" rx="9"/>
        <text class="service-label" x="160" y="380" font-size="50" text-anchor="middle" textLength="156" lengthAdjust="spacingAndGlyphs">TIRES</text>
        <rect class="service-box" x="298" y="325" width="252" height="73" rx="9"/>
        <text class="service-label" x="424" y="380" font-size="50" text-anchor="middle" textLength="226" lengthAdjust="spacingAndGlyphs">SERVICE</text>
        <rect class="service-box" x="579" y="325" width="252" height="73" rx="9"/>
        <text class="service-label" x="705" y="380" font-size="50" text-anchor="middle" textLength="196" lengthAdjust="spacingAndGlyphs">REPAIR</text>
        <rect class="service-box" x="866" y="325" width="225" height="73" rx="9"/>
        <text class="service-label" x="978" y="380" font-size="50" text-anchor="middle" textLength="186" lengthAdjust="spacingAndGlyphs">DIESEL</text>
      </g>

      <rect class="phone-box" x="53" y="426" width="1038" height="167" rx="16" fill="url(#phoneFill)"/>
      <text class="phone-number" x="576" y="572" font-size="142" text-anchor="middle" textLength="1000" lengthAdjust="spacingAndGlyphs">(555) 314 - 2096</text>

      <text class="town" x="573" y="658" font-size="50" text-anchor="middle" textLength="480" lengthAdjust="spacingAndGlyphs">BRIAR-HOLLOW</text>

      <polygon class="photo-truck" points="1301,0 1661,0 1486,698 1126,698" fill="url(#photoFill)" role="img" aria-label="Photo of a lifted custom pickup truck with light bar and off-road tires"/>
      <line class="edge-orange" x1="1211" y1="350" x2="1118" y2="698" stroke="var(--box-orange)" stroke-width="8"/>
      <line class="edge-blue" x1="1671" y1="0" x2="1593" y2="292" stroke="var(--sky-blue)" stroke-width="7"/>

      <polygon class="photo-hex" points="1231,32 1316,81 1316,179 1231,228 1146,179 1146,81" fill="#6e6a64" stroke="#ffffff" stroke-width="6" role="img" aria-label="Photo of tire, wheel and brake rotor"/>
      <polygon class="photo-hex" points="1526,427 1628,486 1628,604 1526,663 1424,604 1424,486" fill="#8a8680" stroke="#ffffff" stroke-width="6" role="img" aria-label="Photo of a sports car on a lift in the shop"/>
    </svg>
  </div>
</div>
</body>
</html>
```